Business Card Design Project

We currently have existing logo. Looking to have nice colorful business cards done.
We would like the name of business, phone, address, email and website

Target Market(s)

25-50

Industry/Entity Type

Business

Requirements
Must have
• We are currently using
Samrakan font for our business name
Rage italic font for tag line..
you may visit our website at www.velmorita.com to get good feel

velmorita means colors in India. google velmorita to get more info

```html
<!DOCTYPE html>
<html lang="en">
<head>
<meta charset="utf-8">
<title>Velmorita Business Card</title>
<link href="https://fonts.googleapis.com/css2?family=Alegreya+Sans:wght@400&display=swap" rel="stylesheet">
<style>
  :root {
    --canvas: #ffffff;
    --card-deep: #5a1510;
    --card-gloss: #73271f;
    --ink: #ffffff;
    --frame-soft: rgba(255, 255, 255, 0.45);
  }
  html, body {
    margin: 0;
    padding: 0;
    width: 1200px;
    height: 1000px;
    overflow: hidden;
    background: var(--canvas);
    font-family: "Alegreya Sans", "Trebuchet MS", sans-serif;
    color: var(--ink);
  }
  .canvas {
    position: relative;
    width: 1200px;
    height: 1000px;
  }
  .card {
    position: absolute;
    width: 484px;
    height: 280px;
    background: var(--card-deep);
    overflow: hidden;
  }
  .card--front { left: 269px; top: 192px; }
  .card--back  { left: 458px; top: 519px; }
  .card__surface {
    position: absolute;
    inset: 0;
  }
  .card__frame {
    position: absolute;
    box-sizing: border-box;
  }
  .card--front .card__frame {
    left: 18px; top: 19px; width: 448px; height: 248px;
    border: 1.2px solid var(--ink);
  }
  .card--back .card__frame {
    left: 41px; top: 31px; width: 402px; height: 218px;
    border: 1px solid var(--frame-soft);
  }
  .brand {
    position: absolute;
    display: flex;
    align-items: center;
    gap: 10px;
    font-weight: 400;
    line-height: 1;
    letter-spacing: 0.5px;
  }
  .brand__dot {
    display: inline-block;
    border-radius: 50%;
    background: var(--ink);
  }
  .card--front .brand { left: 37px; top: 36px; font-size: 44px; }
  .card--front .brand__dot { width: 8px; height: 8px; }
  .card--back .brand { left: 132px; top: 110px; font-size: 34px; }
  .card--back .brand__dot { width: 7px; height: 7px; }
  .contact {
    position: absolute;
    font-size: 13px;
    line-height: 20px;
  }
  .contact--address { left: 30px; top: 136px; }
  .contact--lines { left: 30px; top: 206px; }
  .contact__row { display: flex; }
  .contact__label { width: 56px; }
  .contact__label--tel { width: 66px; }
  .contact--email { right: 48px; top: 226px; }
</style>
</head>
<body>
<div class="canvas">

  <section class="card card--front" aria-label="Business card front">
    <svg class="card__surface" width="484" height="280" viewBox="0 0 484 280" aria-hidden="true">
      <path d="M0,0 H470 C445,8 425,35 385,78 C325,140 210,182 0,195 Z" fill="var(--card-gloss)"/>
    </svg>
    <div class="card__frame"></div>
    <div class="brand"><span class="brand__name">velmorita</span><span class="brand__dot"></span></div>
    <address class="contact contact--address" style="font-style:normal">
      <div>1480 Alder Crest Road</div>
      <div>Fremont, CA</div>
      <div>94538</div>
    </address>
    <div class="contact contact--lines">
      <div class="contact__row"><span class="contact__label contact__label--tel">Telephone:</span><span>510.555.0142</span></div>
      <div class="contact__row"><span class="contact__label contact__label--tel">Fax:</span><span>510.555.0143</span></div>
    </div>
    <div class="contact contact--email">info@velmorita.com</div>
  </section>

  <section class="card card--back" aria-label="Business card back">
    <svg class="card__surface" width="484" height="280" viewBox="0 0 484 280" aria-hidden="true">
      <path d="M0,0 H470 C445,8 425,35 385,80 C325,142 210,186 0,199 Z" fill="var(--card-gloss)"/>
    </svg>
    <div class="card__frame"></div>
    <div class="brand"><span class="brand__name">velmorita</span><span class="brand__dot"></span></div>
  </section>

</div>
</body>
</html>
```